Cobalt Reclaim Partners is a recycling company. We have started a marketing campaign and would love your artwork to help us get started. We would like the fallowing to be on our postcard:
At the top please write: Now servicing businesses in the city of Industry!
Below that we would like 3 pictures.. The first is a picture of trash, the second is a our logo and at plus sign. After that would be a picture of neat baled recycled material and the last picture would be money. Below this please right the following:
- Companies choose cobalt reclaim partners because:
- if it can be recycled we will find a use for it
- we pay top dollar
- starting our service is fast and easy
* All it takes is one call/email and we will handle the rest
At the bottom please put our contact information
- 800.514.2276
- maribel@salvorix27.com
- salvorix27.com

Thanks guys! I have attached our logo!

I am sorry for this late post,but could you not put anything on the back except for a return address which is 1847 Dorrance Ave Costa Mesa, Ca 92926 Thank you! We have had a lot of trouble in the past with the post office when we put stuff on the back for some reason.

```html
<!DOCTYPE html>
<html lang="en">
<head>
<meta charset="utf-8">
<title>Cobalt Reclaim Partners – Postcard</title>
<link rel="stylesheet" href="https://fonts.googleapis.com/css2?family=PT+Sans:wght@400;700&family=Questrial&display=swap">
<style>
  :root {
    --paper: #efefe9;
    --paper-light: #fbfbf8;
    --paper-shade: #dedfd6;
    --ink: #595947;
    --ink-soft: #68685a;
    --rule: #a9a99c;
    --green: #6cb04a;
    --bin-green: #2a8636;
    --bin-dark: #1b6426;
    --money-green: #8e9a78;
    --money-dark: #6d7a5c;
    --money-light: #d3d8c6;
    --trash-tone: #a9a596;
    --trash-light: #dcd9d0;
    --disc-light: #fdfdfb;
    --disc-edge: #e6e6e1;
  }
  * { margin: 0; padding: 0; box-sizing: border-box; }
  html, body { width: 1200px; height: 776px; overflow: hidden; }
  body {
    font-family: "PT Sans", Arial, sans-serif;
    color: var(--ink);
  }
  .postcard {
    position: relative;
    width: 1200px;
    height: 776px;
    overflow: hidden;
    background:
      linear-gradient(160deg, transparent 0 18%, rgba(255,255,255,.6) 24%, transparent 31%),
      linear-gradient(152deg, transparent 0 40%, rgba(255,255,255,.55) 47%, transparent 54%),
      linear-gradient(158deg, transparent 0 56%, rgba(205,206,196,.45) 64%, transparent 73%),
      linear-gradient(150deg, transparent 0 74%, rgba(255,255,255,.5) 80%, transparent 86%),
      linear-gradient(150deg, var(--paper-light), var(--paper) 55%, var(--paper-shade));
  }
  .top-rule {
    position: absolute;
    top: 96px;
    height: 2px;
    background: var(--rule);
  }
  .top-rule.left { left: 30px; width: 388px; }
  .top-rule.right { left: 783px; width: 388px; }

  .brand {
    position: absolute;
    top: 20px;
    left: 0;
    width: 1200px;
    text-align: center;
  }
  .brand-dot {
    display: block;
    width: 60px;
    height: 60px;
    margin: 0 auto;
    border-radius: 50%;
    background: var(--green);
  }
  .brand-name {
    margin-top: 30px;
    font-size: 33px;
    font-weight: 700;
    line-height: 1;
    color: var(--ink);
  }

  .headline {
    position: absolute;
    top: 164px;
    left: 0;
    width: 1200px;
    text-align: center;
    font-family: "Questrial", "Century Gothic", sans-serif;
    font-size: 39px;
    font-weight: 400;
    color: var(--ink);
    letter-spacing: .4px;
  }

  .step {
    position: absolute;
    border-radius: 50%;
    overflow: hidden;
    background: radial-gradient(circle at 40% 35%, var(--disc-light), #f3f3f0 70%, var(--disc-edge));
    box-shadow: 0 6px 14px rgba(0,0,0,.18);
  }
  .step.bin { left: 140px; top: 268px; width: 244px; height: 244px; }
  .step.sort { left: 433px; top: 217px; width: 332px; height: 332px; }
  .step.payout { left: 760px; top: 245px; width: 290px; height: 290px; }

  .photo { position: absolute; }
  .bin .photo {
    inset: 0;
    background: radial-gradient(ellipse 24% 42% at 50% 48%,
      var(--bin-green) 0, var(--bin-dark) 70%, rgba(240,242,238,0) 100%);
  }
  .sort .photo {
    left: 30px; top: 26px; width: 272px; height: 150px;
    background: radial-gradient(ellipse 48% 46% at 52% 56%,
      var(--trash-tone) 0, var(--trash-light) 62%, rgba(248,248,245,0) 100%);
  }
  .payout .photo {
    inset: 0;
    background: radial-gradient(ellipse 46% 32% at 50% 52%,
      var(--money-dark) 0, var(--money-green) 45%, var(--money-light) 80%, rgba(245,245,242,0) 100%);
  }
  .plus {
    position: absolute;
    left: 0; top: 152px; width: 332px;
    text-align: center;
    font-size: 54px;
    line-height: 1;
    color: var(--ink);
  }
  .sort-brand {
    position: absolute;
    left: 0; top: 222px; width: 332px;
    text-align: center;
    font-size: 21px;
    font-weight: 700;
    line-height: 1.15;
    color: var(--ink);
  }

  .flow-arrow {
    position: absolute;
    top: 382px;
    width: 24px;
    height: 24px;
  }
  .flow-arrow.first { left: 398px; }
  .flow-arrow.second { left: 723px; }

  .reasons {
    position: absolute;
    top: 566px;
    left: 0;
    width: 1200px;
    text-align: center;
    text-transform: uppercase;
  }
  .reasons-title {
    display: inline-block;
    font-size: 21px;
    font-weight: 400;
    color: var(--ink);
    letter-spacing: .5px;
    padding: 0 12px 6px;
    border-bottom: 1px solid var(--rule);
    width: 688px;
  }
  .reasons-list {
    list-style: none;
    margin-top: 10px;
    font-size: 17.5px;
    color: var(--ink-soft);
    letter-spacing: .3px;
  }
  .reasons-list li { display: inline; }
  .reasons-list li + li::before {
    content: "";
    display: inline-block;
    width: 9px; height: 9px;
    margin: 0 18px 2px;
    border-radius: 50%;
    background: var(--green);
  }
  .reasons-close {
    margin-top: 3px;
    font-size: 17.5px;
    color: var(--ink-soft);
    letter-spacing: .3px;
  }

  .bottom-rule {
    position: absolute;
    top: 677px;
    left: 30px;
    width: 1140px;
    height: 2px;
    background: var(--rule);
  }

  .contact {
    position: absolute;
    top: 695px;
    display: flex;
    align-items: center;
    gap: 14px;
    font-size: 20px;
    letter-spacing: 1.6px;
    text-transform: uppercase;
    color: var(--ink);
  }
  .contact.phone { left: 35px; }
  .contact.web { left: 458px; }
  .contact.mail { left: 836px; }
  .contact-icon {
    width: 40px; height: 40px;
    border-radius: 50%;
    background: radial-gradient(circle at 40% 35%, #ffffff, #e7e7e2);
    box-shadow: 0 2px 5px rgba(0,0,0,.2);
    display: flex;
    align-items: center;
    justify-content: center;
  }
</style>
</head>
<body>
<main class="postcard">
  <div class="top-rule left"></div>
  <div class="top-rule right"></div>

  <header class="brand">
    <span class="brand-dot"></span>
    <div class="brand-name">Cobalt Reclaim Partners</div>
  </header>

  <h1 class="headline">Now servicing businesses in the city of Industry!</h1>

  <section class="steps">
    <div class="step bin">
      <div class="photo" role="img" aria-label="Green cylindrical recycling bin"></div>
    </div>

    <svg class="flow-arrow first" viewBox="0 0 24 24" aria-hidden="true">
      <circle cx="12" cy="12" r="11" fill="#f4f4f0" stroke="#c4c4bb"/>
      <path d="M9 7 L16 12 L9 17 Z" fill="#b5b5ab"/>
    </svg>

    <div class="step sort">
      <div class="photo" role="img" aria-label="Pile of mixed recyclables: bottles, cans, cardboard and paper"></div>
      <div class="plus">+</div>
      <div class="sort-brand">Cobalt Reclaim<br>Partners</div>
    </div>

    <svg class="flow-arrow second" viewBox="0 0 24 24" aria-hidden="true">
      <circle cx="12" cy="12" r="11" fill="#f4f4f0" stroke="#c4c4bb"/>
      <path d="M9 7 L16 12 L9 17 Z" fill="#b5b5ab"/>
    </svg>

    <div class="step payout">
      <div class="photo" role="img" aria-label="Stacks of banded hundred-dollar bills"></div>
    </div>
  </section>

  <section class="reasons">
    <h2 class="reasons-title">Companies choose Cobalt Reclaim Partners because:</h2>
    <ul class="reasons-list">
      <li>If it can be recycled we will find a use for it</li>
      <li>We pay top dollar</li>
      <li>Starting our service is fast and easy</li>
    </ul>
    <p class="reasons-close">All it takes is one call/email and we will handle the rest</p>
  </section>

  <div class="bottom-rule"></div>

  <footer>
    <div class="contact phone">
      <span class="contact-icon">
        <svg width="22" height="22" viewBox="0 0 24 24" aria-hidden="true">
          <path d="M6.6 10.8a15.2 15.2 0 0 0 6.6 6.6l2.2-2.2a1 1 0 0 1 1-.25 11.4 11.4 0 0 0 3.6.57 1 1 0 0 1 1 1V20a1 1 0 0 1-1 1A17 17 0 0 1 3 4a1 1 0 0 1 1-1h3.5a1 1 0 0 1 1 1c0 1.25.2 2.46.57 3.6a1 1 0 0 1-.25 1z" fill="#6cb04a"/>
        </svg>
      </span>
      <span>800.514.2276</span>
    </div>
    <div class="contact web">
      <span class="contact-icon">
        <svg width="24" height="24" viewBox="0 0 24 24" aria-hidden="true" fill="none" stroke="#6cb04a" stroke-width="1.6">
          <circle cx="12" cy="12" r="9"/>
          <ellipse cx="12" cy="12" rx="4" ry="9"/>
          <path d="M3 12h18M5 7h14M5 17h14"/>
        </svg>
      </span>
      <span>salvorix27.com</span>
    </div>
    <div class="contact mail">
      <span class="contact-icon">
        <svg width="24" height="24" viewBox="0 0 24 24" aria-hidden="true" fill="none" stroke="#6cb04a" stroke-width="2.2">
          <circle cx="12" cy="12" r="3.6"/>
          <path d="M15.6 12v1.6a2.6 2.6 0 0 0 5.2 0V12a8.8 8.8 0 1 0-3.4 6.9"/>
        </svg>
      </span>
      <span>maribel@salvorix27.com</span>
    </div>
  </footer>
</main>
</body>
</html>
```